Silver Brook Home Business Cards

We need Business cards development for our expanding business. Our Company SilverBrookHome promotes grain free living through products, services and healthy living concepts. Our Products are:
Non-Grain
Non- GMO
Non- Soy
Gluten-Free

Project Deadline Extended
Reason: We will need to extend the deadline on our Business Card contest. Thanks, SBH

```html
<!DOCTYPE html>
<html lang="en">
<head>
<meta charset="utf-8">
<title>Silver Brook Home – Business Cards</title>
<link rel="stylesheet" href="https://fonts.googleapis.com/css2?family=Open+Sans:wght@300;400;600;700&display=swap">
<style>
  :root {
    --bg: #1f1f1f;
    --green-deep: #1b6a36;
    --green-mid: #2a8a45;
    --green-light: #72c24c;
    --brand-green: #3a9a2a;
    --white: #ffffff;
    --muted: #8a8a8a;
    --text-light: #e6f2e8;
    --text-soft: #b9d8bf;
  }
  * { box-sizing: border-box; margin: 0; padding: 0; }
  html, body {
    width: 1200px; height: 1000px; overflow: hidden;
    background: var(--bg);
    font-family: "Open Sans", Arial, sans-serif;
  }
  .canvas { position: relative; width: 1200px; height: 1000px; }
  .card {
    position: absolute; left: 250px;
    width: 700px; height: 400px;
    border-radius: 22px; overflow: hidden;
    background: var(--white);
    box-shadow: 0 12px 30px rgba(0,0,0,.45);
  }
  .card--front { top: 70px; }
  .card--contact { top: 530px; }
  .card-shape { position: absolute; inset: 0; width: 100%; height: 100%; }

  .brand {
    position: absolute; left: 300px; top: 150px; width: 380px;
    display: flex; align-items: center; justify-content: center; gap: 12px;
  }
  .brand-dot {
    width: 26px; height: 26px; border-radius: 50%;
    background: var(--brand-green);
  }
  .brand-name {
    color: var(--brand-green); font-weight: 700; font-size: 38px;
    letter-spacing: -0.5px;
  }
  .website {
    position: absolute; left: 300px; top: 300px; width: 380px;
    text-align: center; color: var(--muted);
    font-weight: 300; font-size: 20px; letter-spacing: 1px;
  }

  .product-list {
    position: absolute; left: 60px; top: 150px;
    list-style: none; color: var(--white);
    font-weight: 700; font-size: 19px; line-height: 1.45;
  }
  .product-list li::before { content: "•"; margin-right: 8px; }

  .person {
    position: absolute; left: 44px; top: 44px; color: var(--white);
  }
  .person-name { font-weight: 700; font-size: 26px; }
  .person-role { font-weight: 300; font-size: 16px; color: var(--text-soft); margin-bottom: 10px; }
  .person-line { font-weight: 300; font-size: 17px; color: var(--text-light); line-height: 1.4; }

  .company {
    position: absolute; left: 44px; top: 240px; color: var(--white);
  }
  .company-name { font-weight: 700; font-size: 18px; margin-bottom: 6px; }
  .company-line { font-weight: 300; font-size: 17px; color: var(--text-light); line-height: 1.4; }
</style>
</head>
<body>
<main class="canvas">

  <section class="card card--front" aria-label="Business card front">
    <svg class="card-shape" viewBox="0 0 700 400" aria-hidden="true">
      <defs>
        <linearGradient id="greenFill" x1="0" y1="0" x2="0" y2="1">
          <stop offset="0" stop-color="#1b6a36"/>
          <stop offset="1" stop-color="#2f8f48"/>
        </linearGradient>
      </defs>
      <rect width="700" height="400" fill="url(#greenFill)"/>
      <ellipse cx="600" cy="230" rx="400" ry="360" fill="#72c24c"/>
      <ellipse cx="620" cy="240" rx="385" ry="360" fill="#ffffff"/>
    </svg>
    <ul class="product-list">
      <li>Non-Grain</li>
      <li>Non- GMO</li>
      <li>Non- Soy</li>
      <li>Gluten-Free</li>
    </ul>
    <div class="brand">
      <span class="brand-dot"></span>
      <span class="brand-name">SilverBrookHome</span>
    </div>
    <p class="website">www.silverbrookhome.com</p>
  </section>

  <section class="card card--contact" aria-label="Business card contact side">
    <svg class="card-shape" viewBox="0 0 700 400" aria-hidden="true">
      <defs>
        <linearGradient id="greenFill2" x1="0" y1="0" x2="0" y2="1">
          <stop offset="0" stop-color="#1b6a36"/>
          <stop offset="1" stop-color="#2f8f48"/>
        </linearGradient>
      </defs>
      <rect width="700" height="400" fill="url(#greenFill2)"/>
      <ellipse cx="650" cy="230" rx="340" ry="360" fill="#72c24c"/>
      <ellipse cx="670" cy="240" rx="325" ry="360" fill="#ffffff"/>
    </svg>
    <div class="person">
      <p class="person-name">Daniel Harper</p>
      <p class="person-role">Accountant</p>
      <p class="person-line">+61 3 555 0142</p>
      <p class="person-line">daniel@silverbrookhome.com</p>
    </div>
    <div class="company">
      <p class="company-name">Silver Brook Home LLC</p>
      <p class="company-line">Suite 4/12 Orchard Lane</p>
      <p class="company-line">Brookvale, Australia, 3100</p>
    </div>
    <div class="brand" style="left:370px; width:320px;">
      <span class="brand-dot"></span>
      <span class="brand-name" style="font-size:32px;">SilverBrookHome</span>
    </div>
    <p class="website" style="left:370px; width:320px;">www.silverbrookhome.com</p>
  </section>

</main>
</body>
</html>
```